The Pixel Tap Business card.

A Simple card with our Logo and contact information. To give to investors and other professionals.

We are a nerd themed bar.
our target market is young professionals age 21+ but the real purpose of this business card is to present to potential investors and other professionals with our contact information. as we are still looking for funding before we start up.

I am partial to green and my partner likes red we are open to iteration.

Target Market(s)

Investors

Industry/Entity Type

Business

Contact Information for Business Card

Martin Hale (225) 730-6192 kent.h4711@mailnest.test Glen Porter (225) 968-5037 glenp318@mailnest.test

Font styles to use
Serif

Requirements
Nice to have
• Keep it simple but not boring.
• Use the Logos but feel free to edit them to match theme/colors.
• Keep the back clean and use one of the Logos.

```html
<!DOCTYPE html>
<html lang="en">
<head>
<meta charset="utf-8">
<title>The Pixel Tap – Business Card</title>
<link rel="stylesheet" href="https://fonts.googleapis.com/css2?family=Lato:wght@400;700;900&display=swap">
<style>
  :root {
    --backdrop: #ece9e4;
    --card-white: #ffffff;
    --tint: #fbf1f1;
    --ink: #111111;
    --red: #e21f2b;
    --muted: #333333;
  }
  * { box-sizing: border-box; margin: 0; padding: 0; }
  html, body {
    width: 1200px; height: 900px; overflow: hidden;
    background: var(--backdrop);
    font-family: "Lato", Arial, sans-serif;
    color: var(--ink);
  }
  .stage {
    width: 1200px; height: 900px;
    display: flex; flex-direction: column;
    align-items: center; justify-content: center; gap: 48px;
  }
  .card {
    position: relative;
    width: 660px; height: 380px;
    background: var(--ink);
    padding: 14px;
    box-shadow: 0 10px 24px rgba(0,0,0,.18);
  }
  .card__face {
    position: relative; width: 100%; height: 100%;
    display: flex;
  }
  .card__band { background: var(--red); flex: 0 0 16px; }
  .card__body { position: relative; flex: 1; }

  /* Front */
  .card--front .card__body { background: var(--tint); }
  .brand {
    position: absolute; left: 50%; top: 46%;
    transform: translate(-50%, -50%);
    display: flex; align-items: center; gap: 14px;
    white-space: nowrap;
  }
  .brand__dot {
    width: 30px; height: 30px; border-radius: 50%;
    background: var(--red);
  }
  .brand__name {
    font-weight: 900; font-size: 50px; letter-spacing: 1px;
    text-transform: uppercase; color: var(--ink);
  }
  .contact { position: absolute; line-height: 1.25; }
  .contact__name { font-weight: 700; font-size: 19px; }
  .contact__line { font-size: 15px; color: var(--muted); }
  .contact--left { left: 34px; bottom: 28px; }
  .contact--right { right: 30px; top: 30px; text-align: left; }

  /* Back */
  .card--back .card__face { flex-direction: column; }
  .card--back .card__body { background: var(--card-white); }
  .lockup {
    position: absolute; left: 50%; top: 50%;
    transform: translate(-50%, -50%);
    border: 1.5px solid var(--ink);
    padding: 26px 40px;
    text-align: center; white-space: nowrap;
  }
  .lockup__name {
    font-weight: 900; font-size: 44px; text-transform: uppercase;
    letter-spacing: 1px;
  }
  .lockup__tag {
    margin-top: 6px;
    font-weight: 700; font-size: 15px; letter-spacing: 1.5px;
    text-transform: uppercase;
  }
</style>
</head>
<body>
<main class="stage">
  <section class="card card--front" aria-label="Card front">
    <div class="card__face">
      <div class="card__band"></div>
      <div class="card__body">
        <div class="brand">
          <span class="brand__dot"></span>
          <span class="brand__name">The Pixel Tap</span>
        </div>
        <div class="contact contact--right">
          <p class="contact__name">Glen Porter</p>
          <p class="contact__line">(225) 968-5037</p>
          <p class="contact__line">glenp318@mailnest.test</p>
        </div>
        <div class="contact contact--left">
          <p class="contact__name">Martin Hale</p>
          <p class="contact__line">(225) 730-6192</p>
          <p class="contact__line">kent.h4711@mailnest.test</p>
        </div>
      </div>
    </div>
  </section>

  <section class="card card--back" aria-label="Card back">
    <div class="card__face">
      <div class="card__body">
        <div class="lockup">
          <p class="lockup__name">The Pixel Tap</p>
          <p class="lockup__tag">Lounge and Arcade</p>
        </div>
      </div>
      <div class="card__band"></div>
    </div>
  </section>
</main>
</body>
</html>
```